Brennock Metal recycling, a business card/logo for our industrial family metal recycling company

A new business card design/logo for our long established family metal recycling company.
I have a logo for our property company which was designed a few months ago on pixel forum which I would like to be very close to this design but have a more industrial feel to it and in a darker blue colour, please see attachments.

Target Market(s)

industries that produce metal waste for recycling, construction sites, engineering companies, manufactures, builders, plumbers, electricians, general house holders.

Industry/Entity Type

Recycling

Contact Information for Business Card

owner/director...Gordon brennock
e-mail....info@brennockscrapworks.example.co.uk
web address.....brennockscrapworks.example.co.uk

Font styles to use
Serif
Sans Serif

Colors
0255a3
ffffff

Requirements
Must have
• -dark blue business card on front.
-white on the back, see contact details, e-mail address for metal company.
-to have an industrial feel to it.
-brennock logo as business card attached but (brennock metal recycling)
please remove the little roof/arrow above brennock as this was relevant to property company.
Nice to have
• please see our website brennockscrapworks.example.co.uk with all details
being correct however I would like to refresh the logo to more like the brennock property investment business card logo attached.
Should not have
• should not contain details from property investments card as this design is for the metal recycling company.

```html
<!DOCTYPE html>
<html lang="en">
<head>
<meta charset="utf-8">
<title>Brennock Metal Recycling – business card</title>
<link rel="stylesheet" href="https://fonts.googleapis.com/css2?family=Poppins:wght@300;400;600&display=swap">
<style>
  :root {
    --card-blue: #0c58ad;
    --deep-blue: #0255a3;
    --brand-yellow: #e8b93c;
    --ink-white: #ffffff;
    --ink-dark: #1d2a3a;
    --backdrop: #e9ebee;
  }
  * { margin: 0; padding: 0; box-sizing: border-box; }
  html, body {
    width: 1200px; height: 892px; overflow: hidden;
    background: var(--backdrop);
    font-family: "Poppins", sans-serif;
  }
  .sheet {
    width: 1200px; height: 892px;
    display: flex; flex-direction: column;
    align-items: center; justify-content: center; gap: 40px;
  }
  .card {
    position: relative;
    width: 680px; height: 389px;
    overflow: hidden;
    box-shadow: 0 6px 18px rgba(0,0,0,0.18);
  }
  .card-front { background: var(--card-blue); }
  .card-back { background: var(--ink-white); }

  /* brand lockup: name set in one colour and weight */
  .brand {
    display: flex; align-items: center; gap: 12px;
    font-weight: 600;
    line-height: 1.1;
    text-transform: uppercase;
  }
  .brand-dot { flex: none; border-radius: 50%; }

  .card-front .brand {
    position: absolute; left: 50%; top: 50%;
    transform: translate(-50%, -50%);
    font-size: 34px;
    color: var(--brand-yellow);
  }
  .card-front .brand-dot { width: 58px; height: 58px; background: var(--ink-white); }

  .card-back .brand {
    position: absolute; right: 40px; top: 44px;
    font-size: 16px; gap: 8px;
    color: var(--deep-blue);
  }
  .card-back .brand-dot { width: 30px; height: 30px; background: var(--brand-yellow); }

  .accent-bar {
    position: absolute; left: 0; top: 46px;
    width: 44px; height: 132px;
    background: var(--brand-yellow);
  }
  .holder {
    position: absolute; left: 84px; top: 58px;
  }
  .holder-name {
    color: var(--deep-blue);
    font-weight: 600; font-size: 30px; line-height: 1.1;
  }
  .holder-role {
    color: var(--ink-dark);
    font-weight: 300; font-size: 26px; line-height: 1.2;
  }
  .contact-list {
    position: absolute; left: 84px; top: 190px;
    list-style: none;
  }
  .contact-item {
    display: flex; align-items: center; gap: 14px;
    color: var(--ink-dark);
    font-weight: 300; font-size: 19px;
    height: 42px;
  }
  .contact-icon { width: 20px; height: 20px; flex: none; }
  .contact-icon * { fill: var(--brand-yellow); }
</style>
</head>
<body>
<main class="sheet">

  <section class="card card-front" aria-label="Card front">
    <div class="brand">
      <span class="brand-dot"></span>
      <span class="brand-name">Brennock<br>Metal Recycling</span>
    </div>
  </section>

  <section class="card card-back" aria-label="Card back">
    <div class="accent-bar"></div>
    <div class="brand">
      <span class="brand-dot"></span>
      <span class="brand-name">Brennock<br>Metal Recycling</span>
    </div>

    <div class="holder">
      <p class="holder-name">Gordon brennock</p>
      <p class="holder-role">Director</p>
    </div>

    <ul class="contact-list">
      <li class="contact-item">
        <svg class="contact-icon" viewBox="0 0 24 24" aria-hidden="true"><path d="M6.6 10.8a15.1 15.1 0 0 0 6.6 6.6l2.2-2.2a1 1 0 0 1 1-.25 11.4 11.4 0 0 0 3.6.57 1 1 0 0 1 1 1V20a1 1 0 0 1-1 1A17 17 0 0 1 3 4a1 1 0 0 1 1-1h3.5a1 1 0 0 1 1 1c0 1.25.2 2.45.57 3.570a1 1 0 0 1-.25 1z"/></svg>
        <span>020 7946 0123</span>
      </li>
      <li class="contact-item">
        <svg class="contact-icon" viewBox="0 0 24 24" aria-hidden="true"><path d="M12 2a10 10 0 1 0 0 20 10 10 0 0 0 0-20zm6.9 6h-3a15.6 15.6 0 0 0-1.3-3.6A8 8 0 0 1 18.9 8zM12 4c.8 1.2 1.5 2.5 1.9 4h-3.8c.4-1.5 1.1-2.8 1.9-4zM4.3 14a8 8 0 0 1 0-4h3.4a16.5 16.5 0 0 0 0 4zm.8 2h3a15.6 15.6 0 0 0 1.3 3.6A8 8 0 0 1 5.1 16zm3-8h-3a8 8 0 0 1 4.3-3.6A15.6 15.6 0 0 0 8.1 8zM12 20c-.8-1.2-1.5-2.5-1.9-4h3.8c-.4 1.5-1.1 2.8-1.9 4zm2.3-6H9.7a14.7 14.7 0 0 1 0-4h4.6a14.7 14.7 0 0 1 0 4zm.3 5.6a15.6 15.6 0 0 0 1.3-3.6h3a8 8 0 0 1-4.3 3.6zm1.7-5.6a16.5 16.5 0 0 0 0-4h3.4a8 8 0 0 1 0 4z"/></svg>
        <span>brennockscrapworks.example.co.uk</span>
      </li>
      <li class="contact-item">
        <svg class="contact-icon" viewBox="0 0 24 24" aria-hidden="true"><path d="M3 5h18v2l-9 6-9-6zm0 4.4 9 6 9-6V19H3z"/></svg>
        <span>info@brennockscrapworks.example.co.uk</span>
      </li>
      <li class="contact-item">
        <svg class="contact-icon" viewBox="0 0 24 24" aria-hidden="true"><path d="M12 2a7 7 0 0 0-7 7c0 5.2 7 13 7 13s7-7.8 7-13a7 7 0 0 0-7-7zm0 9.5A2.5 2.5 0 1 1 12 6.5a2.5 2.5 0 0 1 0 5z"/></svg>
        <span>Unit 9, 14B Quarry Lane, London, SE99 1ZZ</span>
      </li>
    </ul>
  </section>

</main>
</body>
</html>
```